Criação de Papelaria Profissional para Construção & Engenharia
" Empresa do ramo da engenharia civil com foco projeto, construção, planejamento, gestão e consultoria de obras de construção civil e todo tipo de atividade correlacionada. "

```html
<!DOCTYPE html>
<html lang="pt-BR">
<head>
<meta charset="UTF-8">
<title>Pedra Alta Projetos – Pasta Institucional</title>
<link href="https://fonts.googleapis.com/css2?family=Cormorant+Garamond:wght@600&family=Montserrat:wght@400;500&display=swap" rel="stylesheet">
<style>
  :root {
    --stage: #4f6a2e;
    --cover-dark: #252a1f;
    --cover-mid: #323a29;
    --cover-light: #3b4531;
    --decor: rgba(120, 140, 95, 0.14);
    --gold: #b8903f;
    --muted: #a9ab9c;
    --spine: rgba(0, 0, 0, 0.35);
  }
  * { margin: 0; padding: 0; box-sizing: border-box; }
  html, body { width: 1200px; height: 1200px; overflow: hidden; }
  body {
    background: var(--stage);
    display: flex; align-items: center; justify-content: center;
    font-family: "Montserrat", sans-serif;
  }
  .folder-spread {
    position: relative;
    width: 940px; height: 660px;
    display: flex;
    background: linear-gradient(160deg, var(--cover-light) 0%, var(--cover-mid) 45%, var(--cover-dark) 100%);
    overflow: hidden;
  }
  .folder-decor {
    position: absolute;
    left: 220px; top: 40px;
    width: 460px; height: 460px;
    border-radius: 50%;
    background: var(--decor);
  }
  .folder-spine {
    position: absolute; left: 50%; top: 0; bottom: 0;
    width: 2px; background: var(--spine);
  }
  .panel { position: relative; width: 50%; height: 100%; }
  .brand {
    position: absolute;
    display: flex; align-items: center; gap: 10px;
  }
  .brand-dot { flex: none; border-radius: 50%; background: var(--gold); }
  .brand-name {
    font-family: "Cormorant Garamond", serif; font-weight: 600;
    color: var(--gold); white-space: nowrap;
  }
  .back-cover .brand { left: 40px; bottom: 72px; }
  .back-cover .brand-dot { width: 16px; height: 16px; }
  .back-cover .brand-name { font-size: 15px; }
  .contact-list {
    position: absolute; left: 200px; bottom: 50px;
    list-style: none; display: flex; flex-direction: column; gap: 7px;
    font-size: 9px; color: var(--muted);
  }
  .contact-list li { display: flex; align-items: center; gap: 7px; }
  .contact-list svg { width: 10px; height: 10px; stroke: var(--muted); fill: none; stroke-width: 1.6; }
  .front-cover .brand { right: 40px; top: 345px; gap: 14px; }
  .front-cover .brand-dot { width: 30px; height: 30px; }
  .front-cover .brand-name { font-size: 30px; }
</style>
</head>
<body>
  <main class="folder-spread">
    <div class="folder-decor" role="img" aria-label="Grande símbolo da marca em marca-d'água sobre a capa"></div>
    <div class="folder-spine"></div>

    <section class="panel back-cover">
      <div class="brand">
        <span class="brand-dot"></span>
        <span class="brand-name">Pedra Alta Projetos</span>
      </div>
      <ul class="contact-list">
        <li><svg viewBox="0 0 12 12"><path d="M2 1.5h2.5l1 2.5-1.5 1a6 6 0 0 0 3 3l1-1.5 2.5 1V11A9 9 0 0 1 1 2.5z"/></svg>11 99999-0000</li>
        <li><svg viewBox="0 0 12 12"><rect x="1" y="2.5" width="10" height="7"/><path d="M1 2.5l5 4 5-4"/></svg>contato@pedraalta.com</li>
        <li><svg viewBox="0 0 12 12"><circle cx="6" cy="6" r="5"/><path d="M1 6h10M6 1c2.5 3 2.5 7 0 10M6 1c-2.5 3-2.5 7 0 10"/></svg>pedraalta.com</li>
        <li><svg viewBox="0 0 12 12"><rect x="1.5" y="1.5" width="9" height="9" rx="2.5"/><circle cx="6" cy="6" r="2.2"/></svg>@pedraaltaprojetos</li>
      </ul>
    </section>

    <section class="panel front-cover">
      <div class="brand">
        <span class="brand-dot"></span>
        <span class="brand-name">Pedra Alta Projetos</span>
      </div>
    </section>
  </main>
</body>
</html>
```